Car rental website design for a UAE car rental company

This project is about creating a new website design for a car rental company located in Dubai (United Arab Emirates), I opened the same project a few months ago but I didn't receive a lot of appealing entries so I closed it but this time I am marking the project as guaranteed to avoid such situation again, if you have already provided a design before then please re-submit again on this project so that it is considered while reviewing all the designs

A few important things:

1- We need a simple non-complex design
2- The final deliverable would be 2 screens (PSD, JPEG ... etc), the first screen is for the home page and the second screen is for an internal page
3- The home page must have a section that end users can use to rent a car online directly from the home page instead of going into some inner pages
4- The current website is very old and not very appealing so avoid creating a similar design (www.runo-vexa.example)
5- The name is Runovexa but the company rents normal cars (no Limousin cars will be rented) so avoid adding any fancy cars in the images/graphics used in the design, just normal end users cars
6- The expected pages would be: home, About us, Our team, Strategy, Contact us and links to social media pages
7- The attachments include the company's logo and some screens from other car rental companies that provide online rentals/payments

If you have any questions please feel free to ask and please note that we will need the designs urgently

Thanks

Target Market(s)

Dubai - United Arab Emirates

Industry/Entity Type

It Company

Number of Pages Required

2 page

Font styles to use
Sans Serif

Requirements
Must have
• Check the project details
Nice to have
Should not have

```html
<!DOCTYPE html>
<html lang="en">
<head>
<meta charset="utf-8">
<title>Runovexa Rent A Car</title>
<link href="https://fonts.googleapis.com/css2?family=Bree+Serif&family=Fjalla+One&family=Roboto:wght@400;500;700&family=Raleway:wght@400;700&display=swap" rel="stylesheet">
<style>
:root{
  --crimson:#b0063a;
  --amber:#f7b52c;
  --ink:#222;
  --light:#f2f2f2;
  --nav:#111;
  --footer:#000;
  --panel:#1b1b1b;
}
*{margin:0;padding:0;box-sizing:border-box}
html,body{width:821px;height:1200px;overflow:hidden;background:#fff}
body{position:relative;font-family:"Roboto",Arial,sans-serif;color:var(--ink)}
.abs{position:absolute}
.topbar{left:0;top:0;width:821px;height:57px;background:linear-gradient(#f4f4f4,#e2e2e2)}
.navbar{left:0;top:57px;width:821px;height:33px;background:linear-gradient(#2a2a2a,var(--nav))}
.brand{left:68px;top:0;width:158px;height:95px;background:#fff;clip-path:polygon(0 0,100% 0,100% 60%,94% 100%,8% 100%,0 60%)}
.brand-name{left:80px;top:52px;width:136px;text-align:center;font-weight:500;font-size:21px;color:var(--crimson)}
.brand-mark{left:134px;top:12px;width:30px;height:30px;background:var(--crimson)}
.phone{left:448px;top:24px;font-size:14px;color:#444;display:flex;align-items:center;gap:6px}
.search{left:584px;top:23px;width:164px;height:18px;border:1px solid #ccc;background:#fff;font-size:7px;color:#666;padding:5px 3px}
.search-btn{left:730px;top:23px;width:18px;height:18px;background:#e4141f}
.nav{left:350px;top:57px;height:33px;display:flex;font-size:9.5px;color:#fff;font-weight:500}
.nav span{padding:12px 16px;border-right:1px solid #333}
.nav span:last-child{border:none}
.hero{left:0;top:90px;width:821px;height:363px;background:linear-gradient(#6f7f95 0%,#c8b7a8 38%,#8b8480 55%,#4d4a48 100%)}
.hero-title{left:63px;top:156px;font-family:"Fjalla One",sans-serif;color:#fff;line-height:1}
.hero-title .l1{font-size:35px}
.hero-title .l2{font-size:46px;margin-top:4px}
.starting{left:229px;top:265px;font-family:"Fjalla One",sans-serif;color:#fff;font-size:20px}
.price{left:298px;top:243px;font-family:"Fjalla One",sans-serif;color:var(--crimson);font-size:44px}
.btn-rent{left:111px;top:322px;width:119px;height:30px;background:var(--crimson);color:#fff;font-weight:700;font-size:12px;text-align:center;line-height:30px}
.btn-contact{left:236px;top:322px;width:114px;height:30px;background:var(--amber);color:#222;font-weight:700;font-size:13px;text-align:center;line-height:30px}
.or{left:224px;top:328px;width:18px;height:18px;border-radius:50%;background:#ddd;font-size:5px;color:#888;text-align:center;line-height:18px}
.book{left:478px;top:130px;width:259px;height:301px;background:rgba(240,240,240,.92)}
.book h2{position:absolute;left:16px;top:10px;font-family:"Bree Serif",serif;font-size:21px;color:var(--crimson);letter-spacing:.5px}
.book .sub{position:absolute;left:16px;top:39px;width:180px;font-size:9.5px;color:#333;line-height:12px}
.field{position:absolute;background:#fff;border:1px solid #e2e2e2;font-size:10px;color:#222;padding:7px 6px}
.lbl{position:absolute;font-size:10px;color:#333}
.cont{position:absolute;left:16px;top:262px;width:223px;height:33px;background:var(--crimson);color:#fff;font-size:14px;text-align:center;line-height:33px;border-radius:2px}
.occ-car{left:66px;top:490px;width:306px;height:180px;background:radial-gradient(ellipse at 50% 55%,#a6a8b6 0%,#8a8c98 45%,#fff 72%)}
.occ-kicker{left:392px;top:483px;font-family:"Bree Serif",serif;font-size:22px;color:#666}
.occ-title{left:392px;top:506px;font-family:"Bree Serif",serif;font-size:35px;color:var(--crimson)}
.occ-text{left:395px;top:553px;width:345px;font-size:9.8px;line-height:15px;color:#333;text-align:justify}
.btn-all{left:392px;top:641px;width:100px;height:33px;background:var(--crimson);color:#fff;font-size:14px;text-align:center;line-height:33px;border-radius:2px}
.vehicles{left:0;top:715px;width:821px;height:332px;background:var(--light)}
.veh-title{left:0;top:738px;width:771px;text-align:center;font-family:"Bree Serif",serif;font-size:21px;color:var(--crimson)}
.card{top:790px;width:169px;height:223px;background:#e6e6e6}
.card .photo{height:114px;background:radial-gradient(ellipse at 50% 55%,#b4b6bc 0%,#9c9ea4 35%,#fff 65%)}
.card .name{font-size:9.5px;text-align:center;margin-top:11px;line-height:13px;color:#222}
.card .buy{width:55px;height:18px;margin:10px auto 0;background:#333;color:#fff;font-size:8px;text-align:center;line-height:18px}
.card .buy.on{background:var(--crimson)}
.card .pax{position:absolute;left:-10px;top:180px;background:#999;color:#fff;font-size:7px;padding:2px 4px;border-radius:3px}
.card .icons{position:absolute;left:5px;top:195px;width:160px;height:22px;border:1px solid #ccc;display:flex;justify-content:space-around;align-items:center}
.card .icons i{width:8px;height:8px;border:1px solid #aaa;border-radius:2px}
.footer{left:0;top:1047px;width:821px;height:153px;background:var(--footer)}
.notch{left:404px;top:1047px;width:14px;height:7px;background:var(--light);clip-path:polygon(0 0,100% 0,50% 100%)}
.contact-panel{left:89px;top:1080px;width:652px;height:82px;background:var(--panel)}
.call-title{left:136px;top:1093px;font-family:"Raleway",sans-serif;font-weight:700;font-size:20px;color:#fff}
.call-num{left:138px;top:1119px;font-family:"Raleway",sans-serif;font-size:12.5px;color:#ddd;letter-spacing:.5px}
.divider{left:276px;top:1092px;width:1px;height:58px;background:#333}
.ask{left:315px;top:1090px;font-family:"Raleway",sans-serif;font-size:14px;color:#fff}
.ask-input{left:314px;top:1111px;width:293px;height:28px;background:#3a3a3a;color:#888;font-size:10px;padding:8px 10px}
.submit{left:615px;top:1112px;width:116px;height:27px;background:#b8101c;color:#fff;font-weight:700;font-size:12.5px;text-align:center;line-height:27px}
.copy{left:0;top:1177px;width:821px;text-align:center;font-size:8px;color:#666}
</style>
</head>
<body>
<header>
  <div class="abs topbar"></div>
  <div class="abs navbar"></div>
  <div class="abs brand"></div>
  <div class="abs brand-mark"></div>
  <div class="abs brand-name">Runovexa</div>
  <div class="abs phone">
    <svg width="14" height="14" viewBox="0 0 14 14"><circle cx="7" cy="7" r="6.2" fill="none" stroke="#d3202a" stroke-width="1.3"/><path d="M4.5 4.2c.3-.4.8-.4 1 0l.6 1c.2.3 0 .6-.2.8l-.3.3c.4.9 1.1 1.6 2 2l.3-.3c.2-.2.5-.4.8-.2l1 .6c.4.2.4.7 0 1-.7.7-1.7.8-2.6.3C5.8 8.9 4.9 8 4.3 6.8c-.5-.9-.4-1.9.2-2.6z" fill="#d3202a"/></svg>
    +971 4 555 0192
  </div>
  <div class="abs search">Site Search</div>
  <div class="abs search-btn"><svg width="18" height="18" viewBox="0 0 18 18"><circle cx="8" cy="8" r="3.2" fill="none" stroke="#fff" stroke-width="1.4"/><path d="M10.3 10.3l3 3" stroke="#fff" stroke-width="1.6"/></svg></div>
  <nav class="abs nav"><span>HOME</span><span>ABOUT US</span><span>DEALER LOGIN</span><span>CERTIFIED STOCK</span><span>ASK US</span></nav>
</header>

<section>
  <div class="abs hero" role="img" aria-label="Grey sedan parked on a cobbled waterfront at dusk under a cloudy sky"></div>
  <div class="abs hero-title"><div class="l1">Top of the line</div><div class="l2">for bottom dollar.</div></div>
  <div class="abs starting">Starting</div>
  <div class="abs price">$42</div>
  <div class="abs btn-rent">RENT A SEDAN</div>
  <div class="abs btn-contact">CONTACT US</div>
  <div class="abs or">OR</div>

  <form class="abs book">
    <h2>BOOK A CAR</h2>
    <p class="sub">of comfort,pleasure and &nbsp;leisure from the best</p>
    <div class="field" style="left:8px;top:67px;width:243px;height:29px">Enter airport, city or zip code</div>
    <div class="field" style="left:8px;top:107px;width:16px;height:16px;padding:0"></div>
    <div class="lbl" style="left:30px;top:109px">Return at diffrent Location</div>
    <div class="lbl" style="left:13px;top:143px">Pick-up date</div>
    <div class="lbl" style="left:165px;top:143px">Drop-off date</div>
    <div class="field" style="left:8px;top:161px;width:83px;height:29px;padding:0"><svg style="margin:8px 0 0 6px" width="11" height="11" viewBox="0 0 11 11"><rect x="1" y="2" width="9" height="8" fill="none" stroke="#3a8ee6"/><rect x="1" y="2" width="9" height="2" fill="#3a8ee6"/><path d="M3 6h1M5 6h1M7 6h1M3 8h1M5 8h1" stroke="#3a8ee6"/></svg></div>
    <div class="field" style="left:96px;top:161px;width:28px;height:29px"></div>
    <div class="field" style="left:131px;top:161px;width:83px;height:29px;padding:0"><svg style="margin:8px 0 0 6px" width="11" height="11" viewBox="0 0 11 11"><rect x="1" y="2" width="9" height="8" fill="none" stroke="#3a8ee6"/><rect x="1" y="2" width="9" height="2" fill="#3a8ee6"/><path d="M3 6h1M5 6h1M7 6h1M3 8h1M5 8h1" stroke="#3a8ee6"/></svg></div>
    <div class="field" style="left:221px;top:161px;width:30px;height:29px"></div>
    <div class="lbl" style="left:13px;top:207px">Car Type</div>
    <div class="field" style="left:8px;top:224px;width:243px;height:29px;padding:8px 8px">Standard<span style="float:right;font-size:7px">&#9660;</span></div>
    <div class="cont">Continue</div>
  </form>
</section>

<section>
  <div class="abs occ-car" role="img" aria-label="Silver compact SUV, front three-quarter view"></div>
  <div class="abs occ-kicker">Rent exclusive car for your</div>
  <div class="abs occ-title">special occasion!</div>
  <p class="abs occ-text">Lorem ipsum dolor sit amet conse ctetur adipisicing elit, sed do eiusmod tempor incididunt ut labore et dolore magna aliqua. Ut enim ad minim veniam, quis nostrud exercitation ullamco laboris nisi ut aliquip ex ea commodo conse-quat. Duis aute irure dolor in reprehenderit in voluptate velit esse cillum dolore eu fugiat nulla pariatur.</p>
  <div class="abs btn-all">See All Cars</div>
</section>

<section>
  <div class="abs vehicles"></div>
  <h2 class="abs veh-title">OUR VEHICLES</h2>
  <svg class="abs" style="left:61px;top:819px" width="35" height="35" viewBox="0 0 35 35"><rect x="8" y="8" width="19" height="19" transform="rotate(45 17.5 17.5)" fill="none" stroke="#111" stroke-width="2"/><path d="M19.5 13l-4.5 4.5 4.5 4.5" fill="none" stroke="#111" stroke-width="2"/></svg>
  <svg class="abs" style="left:712px;top:874px" width="35" height="35" viewBox="0 0 35 35"><rect x="8" y="8" width="19" height="19" transform="rotate(45 17.5 17.5)" fill="none" stroke="#111" stroke-width="2"/><path d="M15.5 13l4.5 4.5-4.5 4.5" fill="none" stroke="#111" stroke-width="2"/></svg>

  <article class="abs card" style="left:114px">
    <div class="photo" role="img" aria-label="Silver sedan, side view"></div>
    <div class="name">SEDRA COMFORT 2.0 D<br>INR. 5,00,000</div>
    <div class="buy">BUY IT</div>
    <span class="pax">5 passengers</span>
    <div class="icons"><i></i><i></i><i></i><i></i><i></i></div>
  </article>
  <article class="abs card" style="left:310px">
    <div class="photo" role="img" aria-label="Silver compact SUV, front three-quarter view"></div>
    <div class="name">SEDRA COMFORT 2.0 D<br>INR. 5,00,000</div>
    <div class="buy on">BUY IT</div>
    <span class="pax">5 passengers</span>
    <div class="icons"><i></i><i></i><i></i><i></i><i></i></div>
  </article>
  <article class="abs card" style="left:507px">
    <div class="photo" role="img" aria-label="Silver sedan, side view"></div>
    <div class="name">SEDRA COMFORT 2.0 D<br>INR. 5,00,000</div>
    <div class="buy">BUY IT</div>
    <span class="pax">5 passengers</span>
    <div class="icons"><i></i><i></i><i></i><i></i><i></i></div>
  </article>
</section>

<footer>
  <div class="abs footer"></div>
  <div class="abs notch"></div>
  <div class="abs contact-panel"></div>
  <svg class="abs" style="left:102px;top:1098px" width="36" height="46" viewBox="0 0 36 46"><path d="M6 4c2-2 4-2 5 0l3 6c1 2 0 3-1 4l-2 2c2 6 6 11 12 14l2-2c1-1 3-2 4-1l5 4c2 1 2 3 0 5-3 3-8 4-12 1C13 32 6 24 3 15 2 10 3 7 6 4z" fill="#c4101c"/><ellipse cx="20" cy="43" rx="11" ry="2" fill="#555"/></svg>
  <div class="abs call-title">CALL US</div>
  <div class="abs call-num">+971 4 555 0192</div>
  <div class="abs divider"></div>
  <div class="abs ask">ASK ?</div>
  <div class="abs ask-input">How can i select a car ?</div>
  <div class="abs submit">Submit</div>
  <div class="abs copy">©Copyright 2011, Runovexa. All rights reserved.</div>
</footer>
</body>
</html>
```